Billboard Design for Modern Dispensary

Hello!
We need a eye-catching 12' x 24' billboard designed for a very successful, modern cannabis dispensary on the Oregon coast, United States. Because of rules, we cannot have any marijuana leafs or other cannabis related images (flower, joints, smoke, etc). We can use the words "Shop" or "Dispensary" - we cannot use the words "cannabis", "marijuana".

Some ideas we had are 3 words stacked on left or center of billboard - maybe across bottom we have horizontal logo and the following words - “North of harbor in Gull Cove”
Another idea is to have a small bubble in bottom/top corner with image of our dog (face only) - with some words around it - like "BONUS Shop Dog" or "Cute Shop Dog" or "Best Shop Dog" or "Friendly Staff"

here's some 3 word examples:
ENJOY
YOUR
TRIP

or

FEEL
GOOD
JUST
AHEAD

or

GOOD
VIBES
ONLY

or

GOOD
TIMES
CHILL
VIBES

I have attached our logo. I have also included a stacked logo version (vertical, not horizontal). the formats are .EPS and .PDF - the logos were created in Affinity Design 2.x.

Our website is coralnook.net if you want to see more images, etc about our dispensary.

Artwork Requirements:
The billboard is 12' tall x 25' wide
The artwork needs to be 1”=1’ @ 300dpi
Please add 6” of bleed all around so your total artwork is 13”x26”
Final deliverable should be .Ai file.

Font styles to use
Sans Serif

Colors
0054AA
0677BA
7BADD7
CADEEF
E8F1F8

Requirements
Nice to have
• See the project description - we included some ideas to consider.
Should not have
• No cannabis images, like flower, cannabis leaves, paraphenlia, cartridges, joints, etc.

```html
<!DOCTYPE html>
<html lang="en">
<head>
<meta charset="utf-8">
<title>Coral Nook Billboard</title>
<link rel="stylesheet" href="https://fonts.googleapis.com/css2?family=Poppins:wght@400;600&display=swap">
<style>
  :root {
    --backdrop: #a5a8ab;
    --brand-blue: #3a98d8;
    --ink: #0a0a0a;
    --white: #ffffff;
    --sky-deep: #4a7fcc;
    --sky-mid: #8fb6ec;
    --sky-glow: #f4f7fd;
    --water: #5f86b0;
    --mountain: #3f5872;
  }
  * { margin: 0; padding: 0; box-sizing: border-box; }
  html, body {
    width: 1200px;
    height: 1200px;
    overflow: hidden;
    background: var(--backdrop);
    font-family: "Poppins", sans-serif;
  }
  .billboard {
    position: absolute;
    left: 22px;
    top: 311px;
    width: 1155px;
    height: 578px;
    overflow: hidden;
  }
  .scenery {
    position: absolute;
    inset: 0;
    background:
      radial-gradient(ellipse 42% 52% at 53% 58%, var(--sky-glow) 0%, rgba(244,247,253,0.6) 40%, rgba(244,247,253,0) 100%),
      linear-gradient(to bottom, var(--sky-mid) 0%, #b9d2f3 55%, var(--mountain) 76%, var(--water) 84%, #7e9fc2 100%),
      linear-gradient(to right, var(--sky-mid), var(--sky-deep));
  }
  .brand-panel {
    position: absolute;
    left: 0;
    top: 0;
    width: 561px;
    height: 165px;
  }
  .brand-panel svg { position: absolute; inset: 0; }
  .brand-name {
    position: absolute;
    left: 172px;
    top: 54px;
    font-weight: 400;
    font-size: 44px;
    line-height: 1;
    letter-spacing: 1px;
    color: var(--brand-blue);
    white-space: nowrap;
  }
  .headline {
    position: absolute;
    left: 0;
    right: 0;
    top: 210px;
    text-align: center;
    font-weight: 600;
    font-size: 52px;
    line-height: 1.2;
    color: var(--ink);
    white-space: nowrap;
  }
  .subline {
    position: absolute;
    left: 0;
    right: 0;
    top: 276px;
    text-align: center;
    font-weight: 400;
    font-size: 39px;
    line-height: 1.2;
    color: var(--ink);
  }
  .signoff {
    position: absolute;
    right: 38px;
    top: 494px;
    font-weight: 600;
    font-size: 36px;
    line-height: 1.2;
    color: var(--white);
  }
</style>
</head>
<body>
  <main class="billboard">
    <div class="scenery" role="img" aria-label="Photo of a sunlit coastal inlet with mountains, forested cliffs and a winding road under a blue sky"></div>

    <div class="brand-panel">
      <svg width="561" height="165" viewBox="0 0 561 165" aria-hidden="true">
        <polygon points="0,0 561,0 507,165 0,165" fill="#ffffff"/>
        <circle cx="100" cy="82" r="56" fill="none" stroke="#3a98d8" stroke-width="9"/>
      </svg>
      <div class="brand-name">CORAL NOOK</div>
    </div>

    <h1 class="headline">North of harbor in Gull Cove</h1>
    <p class="subline">Best Dispensary Period</p>
    <p class="signoff">... enjoy your trip</p>
  </main>
</body>
</html>
```